Bref créative
Lemon Badger
Cakes and Desserts
Bright & Fun-filled
Marla Tevison
Owner
2193 Brennick Ct.
Arvada, CO 80005
marla.tevison@postvale.net
Join us on Facebook!
I also need stationery that ties in with my business card.
Logo for cake company

```html
<!DOCTYPE html>
<html lang="en">
<head>
<meta charset="utf-8">
<title>Lemon Badger – Business Cards</title>
<link rel="stylesheet" href="https://fonts.googleapis.com/css2?family=Cinzel:wght@400;600&family=Open+Sans:wght@400;700&display=swap">
<style>
  :root {
    --stage: #e9dfd2;
    --brown: #8b3f22;
    --pink: #e6418f;
    --white: #ffffff;
    --ink: #5a2a18;
    --label: #3b2a20;
  }
  * { box-sizing: border-box; margin: 0; padding: 0; }
  html, body { width: 1200px; height: 794px; overflow: hidden; }
  body {
    background: var(--stage);
    font-family: "Open Sans", Arial, sans-serif;
    position: relative;
  }
  .card {
    position: absolute;
    width: 545px;
    height: 310px;
    border-radius: 16px;
    overflow: hidden;
    box-shadow: 0 2px 6px rgba(0,0,0,.18);
  }
  .card svg.card-bg { position: absolute; inset: 0; width: 100%; height: 100%; }
  .front-a { left: 38px; top: 43px; }
  .front-b { left: 620px; top: 43px; }
  .back-a  { left: 38px; top: 413px; }
  .back-b  { left: 620px; top: 413px; }

  .brand {
    position: absolute;
    display: flex;
    align-items: center;
    gap: 12px;
  }
  .brand-mark { width: 22px; height: 22px; background: var(--pink); }
  .brand-name {
    font-weight: 700;
    font-size: 38px;
    line-height: 1;
    color: var(--ink);
    white-space: nowrap;
  }
  .on-dark .brand-name { color: var(--white); }
  .front .brand { left: 26px; top: 40px; }
  .back .brand { left: 50%; top: 100px; transform: translateX(-50%); }

  .holder {
    position: absolute;
    right: 30px;
    top: 110px;
    font-weight: 700;
    font-size: 17px;
    color: var(--ink);
  }
  .front-b .holder { color: var(--pink); }

  .contact {
    position: absolute;
    left: 300px;
    top: 225px;
    font-size: 13px;
    line-height: 18px;
    color: var(--ink);
    list-style: none;
  }
  .front-b .contact { color: var(--white); left: 292px; }
  .contact b { color: var(--pink); font-weight: 700; }
  .front-b .contact b { color: var(--white); }

  .web {
    position: absolute;
    left: 0; right: 0;
    top: 248px;
    text-align: center;
    font-size: 13px;
    color: var(--ink);
  }
  .back-b .web { color: var(--white); }

  .label {
    position: absolute;
    width: 545px;
    text-align: center;
    font-family: "Cinzel", "Times New Roman", serif;
    font-weight: 600;
    font-size: 22px;
    letter-spacing: 3px;
    color: var(--label);
  }
  .label-front-a { left: 38px; top: 366px; }
  .label-front-b { left: 620px; top: 366px; }
  .label-back-a  { left: 38px; top: 736px; }
  .label-back-b  { left: 620px; top: 736px; }
</style>
</head>
<body>

  <section class="card front front-a">
    <svg class="card-bg" viewBox="0 0 545 310" preserveAspectRatio="none" aria-hidden="true">
      <rect width="545" height="310" fill="var(--white)"/>
      <path d="M0,120 C130,150 230,225 300,310 L0,310 Z" fill="var(--brown)"/>
      <path d="M0,168 C95,190 175,240 215,310" fill="none" stroke="var(--white)" stroke-width="12"/>
    </svg>
    <div class="brand"><span class="brand-mark"></span><span class="brand-name">Lemon Badger</span></div>
    <p class="holder">Marla Tevison</p>
    <ul class="contact">
      <li><b>P:</b> (720) 555-0147</li>
      <li><b>E:</b> marla.tevison@postvale.net</li>
      <li><b>W:</b> www.lemonbadgercakes.com</li>
    </ul>
  </section>

  <section class="card front front-b">
    <svg class="card-bg" viewBox="0 0 545 310" preserveAspectRatio="none" aria-hidden="true">
      <rect width="545" height="310" fill="var(--brown)"/>
      <path d="M0,120 C80,160 135,230 165,310 L0,310 Z" fill="var(--pink)"/>
      <path d="M0,125 C85,165 140,235 172,310" fill="none" stroke="var(--white)" stroke-width="10"/>
    </svg>
    <div class="brand on-dark"><span class="brand-mark"></span><span class="brand-name">Lemon Badger</span></div>
    <p class="holder">Marla Tevison</p>
    <ul class="contact">
      <li><b>P:</b> (720) 555-0147</li>
      <li><b>E:</b> marla.tevison@postvale.net</li>
      <li><b>W:</b> www.lemonbadgercakes.com</li>
    </ul>
  </section>

  <section class="card back back-a">
    <svg class="card-bg" viewBox="0 0 545 310" preserveAspectRatio="none" aria-hidden="true">
      <rect width="545" height="310" fill="var(--white)"/>
    </svg>
    <div class="brand"><span class="brand-mark"></span><span class="brand-name">Lemon Badger</span></div>
    <p class="web">www.lemonbadgercakes.com</p>
  </section>

  <section class="card back back-b">
    <svg class="card-bg" viewBox="0 0 545 310" preserveAspectRatio="none" aria-hidden="true">
      <rect width="545" height="310" fill="var(--brown)"/>
    </svg>
    <div class="brand on-dark"><span class="brand-mark"></span><span class="brand-name">Lemon Badger</span></div>
    <p class="web">www.lemonbadgercakes.com</p>
  </section>

  <p class="label label-front-a">Business Card Front A</p>
  <p class="label label-front-b">Business Card Front B</p>
  <p class="label label-back-a">Business Card Back A</p>
  <p class="label label-back-b">Business Card Back B</p>

</body>
</html>
```